The Willowmere Clinic Flyer Design

The Willowmere Clinic is a new company providing Dietetic services for people with gastrointestinal disorders. The main client base would be people suffering from Irritable Bowel Syndrome. IBS is a collection of symptoms which (will be individual to the suffer) including constipation/diarrhoea/abdominal pain or discomfort/bloating/belching/flatulence/stomach gurgling/reflux/nausea/urgency/incomplete emptying/fatigue/headaches. IBS affects approx 30% of the population. Previous treatments have generally been ineffectual and include medication, hypnotherapy, healthy eating.
Recently it has been found that the FODMAP diet (a diet low in fermentable Carbohydrates) has been effective in 75% of sufferers.
The Low FODMAP diet is complex and it is highly recommended that it is undertaken only under the supervision of a suitably qualified dietitian. Treatment is available within the QRV but is usually accessible only following consultation with a Gastroenterologist. Most GP's have never heard of this treatment as the research was only published in 2009 in Australia and is yet to filter through to the general practitioner. The Willowmere Clinic is the only clinic in the UK offering dietetic lead specialist services.
I am a member of the ZLO and MVRT (logos provided)
The flyer would be double sided, informing the patient of all the self help steps they could take if they have IBS then recommending that they contact The Willowmere Clinic for specialist advice.
Self Help: Healthy eating, regular meals, good intake of non caffeinated non alcoholic non fizzy drinks, regular exercise, stress management.
The flyer would be left in GP surgeries, Health centres, holistic therapy centres, or through doors.
Target Market(s)
Majority female aged 20-50, able to pay for private services
Industry/Entity Type
Clinic
Look and feel
Each slider illustrates characteristics of the customer's brand and the style your logo design should communicate.

```html
<!DOCTYPE html>
<html lang="en">
<head>
<meta charset="utf-8">
<title>IBS – The Willowmere Clinic Flyer</title>
<link rel="stylesheet" href="https://fonts.googleapis.com/css2?family=Quattrocento:wght@400;700&display=swap">
<style>
  :root {
    --backdrop: #262626;
    --band-blue: #84b5d5;
    --divider: #ffffff;
    --text-light: #ffffff;
    --text-dark: #111111;
    --photo-skin: #c4926f;
    --photo-skin-light: #dcb596;
    --photo-bg: #ecebea;
  }
  * { margin: 0; padding: 0; box-sizing: border-box; }
  html, body {
    width: 1200px; height: 1000px; overflow: hidden;
    background: var(--backdrop);
    font-family: "Quattrocento", Georgia, serif;
  }
  .canvas { position: relative; width: 1200px; height: 1000px; }
  .flyer {
    position: absolute; left: 361px; top: 101px;
    width: 549px; height: 777px;
    background: var(--divider);
  }
  .header-band {
    position: absolute; left: 0; top: 0; width: 549px; height: 137px;
    background: var(--band-blue);
  }
  .headline {
    position: absolute; left: 8px; top: 4px;
    font-size: 100px; line-height: 1; font-weight: 400;
    letter-spacing: 14px; color: var(--text-light);
  }
  .headline-sub {
    position: absolute; left: 7px; top: 101px;
    font-size: 17px; color: var(--text-light);
  }
  .logo-slot {
    position: absolute; left: 447px; top: 53px;
    font-size: 17px; color: var(--text-dark);
  }
  .hero-photo {
    position: absolute; left: 0; top: 141px; width: 549px; height: 365px;
    background:
      radial-gradient(ellipse 46% 70% at 50% 62%, var(--photo-skin-light) 0%, var(--photo-skin) 60%, rgba(196,146,111,0) 100%),
      var(--photo-bg);
  }
  .info-band {
    position: absolute; left: 0; top: 511px; width: 549px; height: 266px;
    background: var(--band-blue); color: var(--text-light);
  }
  .clinic-name {
    position: absolute; left: 0; top: 6px; width: 549px;
    text-align: center; font-size: 44px; font-weight: 400;
  }
  .clinic-tagline {
    position: absolute; left: 0; top: 62px; width: 549px;
    text-align: center; font-size: 15px;
  }
  .address-icon { position: absolute; left: 175px; top: 106px; }
  .address {
    position: absolute; left: 220px; top: 107px;
    font-size: 15px; line-height: 18px; font-style: normal;
  }
  .phone-icon { position: absolute; left: 186px; top: 172px; }
  .phone {
    position: absolute; left: 218px; top: 175px; font-size: 20px;
  }
  .web-icon { position: absolute; left: 122px; top: 218px; }
  .website {
    position: absolute; left: 151px; top: 221px;
    font-size: 17px; font-weight: 700;
  }
</style>
</head>
<body>
<div class="canvas">
  <article class="flyer">
    <header class="header-band">
      <h1 class="headline">IBS</h1>
      <p class="headline-sub">Irritable Bowel Syndrome</p>
      <p class="logo-slot">LOGO</p>
    </header>

    <div class="hero-photo" role="img" aria-label="Photo of a woman's bare midriff with a rope tied in a knot around the waist"></div>

    <section class="info-band">
      <h2 class="clinic-name">The Willowmere Clinic</h2>
      <p class="clinic-tagline">is the only clinic in the UK offering dietetic lead specialist services</p>

      <svg class="address-icon" width="34" height="52" viewBox="0 0 34 52" aria-hidden="true">
        <path d="M17 1C8 1 1 8 1 17c0 11 16 34 16 34s16-23 16-34C33 8 26 1 17 1z" fill="#fff"/>
        <circle cx="17" cy="17" r="6" fill="var(--band-blue)"/>
      </svg>
      <address class="address">
        The Willowmere Clinic<br>
        14 Larkspur Lane<br>
        Bristol BS9 7QX
      </address>

      <svg class="phone-icon" width="16" height="24" viewBox="0 0 16 24" aria-hidden="true">
        <path d="M4 1c-2 1-3 3-3 6 0 6 4 13 9 16 2 1 4 0 5-2l-3-5-3 2C7 16 5 11 5 8l3-1L6 1z" fill="#fff"/>
      </svg>
      <p class="phone">070-555-218-93</p>

      <svg class="web-icon" width="22" height="22" viewBox="0 0 22 22" aria-hidden="true" fill="none" stroke="#e8f1f8" stroke-width="1.2">
        <circle cx="11" cy="11" r="10"/>
        <ellipse cx="11" cy="11" rx="4.5" ry="10"/>
        <line x1="1" y1="11" x2="21" y2="11"/>
        <line x1="3" y1="6" x2="19" y2="6"/>
        <line x1="3" y1="16" x2="19" y2="16"/>
      </svg>
      <p class="website">www.willowmereclinic.com</p>
    </section>
  </article>
</div>
</body>
</html>
```